Delcourt Realty Business Cards

Design business card

Target Market(s)

High-End Buyer of Real Estate over $1 million dollars

Industry/Entity Type

Realtor

Contact Information for Business Card

Lena Delcourt R(S) LIC.# 41972
Cell 555 246-1938
Email Lena@Delcourt.example
Website IsleFreshHomes.example

Also Need Cards for:

Hank Delcourt R(B) LIC# 69418
C 555 613-7052
E Hank@Delcourt.example
W IsleFreshHomes.example

Colors

Designer to choose colors to be used in the design.

Requirements
Must have
• Address on back:
• 287 Pohaku Cir. , Wailea HI 96753
• Logo on back
Nice to have
• I would like the phone numbers and email address to be big so people can read it easily
Should not have
• Very small print Except For: address (287 Pohaku Cir. Wailea HI 96753)

```html
<!DOCTYPE html>
<html lang="en">
<head>
<meta charset="utf-8">
<title>Delcourt Realty Business Cards</title>
<link rel="stylesheet" href="https://fonts.googleapis.com/css2?family=Raleway:wght@300;400;600;700&display=swap">
<style>
:root{
  --backdrop:#2a2a2b;
  --card:#f4f4f4;
  --card-edge:#e2e2e2;
  --ink:#111111;
  --ink-soft:#3a3a3a;
  --photo-top:#d9d4cf;
  --photo-mid:#b98a6c;
  --photo-low:#c0356a;
}
*{box-sizing:border-box;margin:0;padding:0}
html,body{width:1200px;height:560px;overflow:hidden;background:var(--backdrop)}
body{position:relative;font-family:"Raleway",Arial,sans-serif;color:var(--ink)}
.card{position:absolute;width:400px;height:228px;border-radius:16px;background:linear-gradient(160deg,#ffffff 0%,var(--card) 55%,var(--card-edge) 100%);overflow:hidden}
.card-back{display:flex;flex-direction:column;align-items:center;justify-content:center}
.brand{display:flex;align-items:center;gap:10px;font-weight:700;letter-spacing:.18em;text-transform:uppercase;color:var(--ink)}
.brand-mark{display:block;background:var(--ink)}
.brand-large{font-size:20px}
.brand-large .brand-mark{width:26px;height:26px;border-radius:3px}
.address{position:absolute;bottom:22px;left:0;right:0;text-align:center;font-size:9px;font-weight:600;letter-spacing:.06em;text-transform:uppercase;color:var(--ink-soft)}
.brand-small{position:absolute;top:16px;right:18px;font-size:10px;gap:6px;letter-spacing:.14em}
.brand-small .brand-mark{width:14px;height:14px;border-radius:2px}
.agent{position:absolute;left:26px;top:70px}
.agent-name{font-size:16px;letter-spacing:.04em;text-transform:uppercase;white-space:nowrap}
.agent-name .first{font-weight:300}
.agent-name .last{font-weight:700}
.agent-name .title{font-weight:700;font-size:12px}
.license{font-size:9px;font-weight:600;margin-top:3px;padding-bottom:4px;border-bottom:1.5px solid var(--ink);width:56px;white-space:nowrap}
.contacts{position:absolute;left:26px;bottom:22px;list-style:none;display:flex;flex-direction:column;gap:5px}
.contacts li{display:flex;align-items:center;gap:7px;font-size:12px;font-weight:600;color:var(--ink)}
.contacts svg{width:11px;height:11px;flex:none}
.photo{position:absolute;right:0;bottom:0;width:170px;height:160px;background:linear-gradient(180deg,var(--photo-top) 0%,var(--photo-mid) 55%,var(--photo-low) 100%)}
.pair-a .card-back{left:40px;top:34px}
.pair-a .card-front{left:170px;top:296px}
.pair-b .card-back{left:630px;top:34px}
.pair-b .card-front{left:760px;top:296px}
</style>
</head>
<body>

<section class="pair pair-a">
  <article class="card card-back">
    <div class="brand brand-large"><span class="brand-mark"></span>Delcourt Realty</div>
    <p class="address">287 Pohaku Cir. , Wailea HI 96753</p>
  </article>
  <article class="card card-front">
    <div class="brand brand-small"><span class="brand-mark"></span>Delcourt Realty</div>
    <div class="agent">
      <h2 class="agent-name"><span class="first">Hank</span> <span class="last">Delcourt</span> <span class="title">R(B)</span></h2>
      <p class="license">LIC.# 69418</p>
    </div>
    <ul class="contacts">
      <li><svg viewBox="0 0 12 12"><path d="M1 4c0-2 2-3 5-3s5 1 5 3l-2 1-1-2H4L3 5z M2 6h8v5H2z" fill="currentColor"/></svg>555 613-7052</li>
      <li><svg viewBox="0 0 12 12"><rect x="1" y="2.5" width="10" height="7" fill="currentColor"/><path d="M1 2.5l5 4 5-4" stroke="#fff" fill="none"/></svg>Hank@Delcourt.example</li>
      <li><svg viewBox="0 0 12 12"><circle cx="6" cy="6" r="5" fill="none" stroke="currentColor"/><ellipse cx="6" cy="6" rx="2" ry="5" fill="none" stroke="currentColor"/><path d="M1 6h10" stroke="currentColor"/></svg>IsleFreshHomes.example</li>
    </ul>
    <div class="photo" role="img" aria-label="Portrait photo of the two agents smiling"></div>
  </article>
</section>

<section class="pair pair-b">
  <article class="card card-back">
    <div class="brand brand-large"><span class="brand-mark"></span>Delcourt Realty</div>
    <p class="address">287 Pohaku Cir. , Wailea HI 96753</p>
  </article>
  <article class="card card-front">
    <div class="brand brand-small"><span class="brand-mark"></span>Delcourt Realty</div>
    <div class="agent">
      <h2 class="agent-name"><span class="first">Lena</span> <span class="last">Delcourt</span> <span class="title">R(S)</span></h2>
      <p class="license">LIC.# 41972</p>
    </div>
    <ul class="contacts">
      <li><svg viewBox="0 0 12 12"><path d="M1 4c0-2 2-3 5-3s5 1 5 3l-2 1-1-2H4L3 5z M2 6h8v5H2z" fill="currentColor"/></svg>555 246-1938</li>
      <li><svg viewBox="0 0 12 12"><rect x="1" y="2.5" width="10" height="7" fill="currentColor"/><path d="M1 2.5l5 4 5-4" stroke="#fff" fill="none"/></svg>Lena@Delcourt.example</li>
      <li><svg viewBox="0 0 12 12"><circle cx="6" cy="6" r="5" fill="none" stroke="currentColor"/><ellipse cx="6" cy="6" rx="2" ry="5" fill="none" stroke="currentColor"/><path d="M1 6h10" stroke="currentColor"/></svg>IsleFreshHomes.example</li>
    </ul>
    <div class="photo" role="img" aria-label="Portrait photo of the two agents smiling"></div>
  </article>
</section>

</body>
</html>
```